Dental Business Card Design

Need to have a business card designed around my logo. I would like to have a unique, professional, and, eye catching designs. Can be associated with the colors within the logo, but not required and would actually like to see other color combinations that may work well with the logo. The back of the card is going to be an appointment reminder. I can provide you with the specific information for that needs to be on the back of the card if it's important for the design. i am an Oral Surgeon and the Business name is "Cedar Hollow Oral Surgery" The logo does have the name already incorporated into the design, however, if changing the fonts I would like to have the "Oral Surgery" emphasized. Please feel free to contact me with any questions as this is very important. I don't want to have any typical dental "tooth, mirror, etc." on the business card. Thank you.

```html
<!DOCTYPE html>
<html lang="en">
<head>
<meta charset="utf-8">
<title>Cedar Hollow Oral Surgery – Appointment Card</title>
<link rel="stylesheet" href="https://fonts.googleapis.com/css2?family=Arimo:wght@400;700&family=Roboto+Condensed:wght@400&display=swap">
<style>
  :root {
    --ink: #111111;
    --paper: #ffffff;
    --blue-deep: #0a3c9e;
    --blue-bright: #3a8ee3;
    --aqua: #a8f3ec;
    --aqua-soft: #d9fbf7;
    --highlight: #fff27a;
  }
  * { margin: 0; padding: 0; box-sizing: border-box; }
  html, body { width: 686px; height: 1200px; overflow: hidden; background: var(--paper); }
  .card {
    position: relative;
    width: 686px;
    height: 1200px;
    background: var(--paper);
    color: var(--ink);
    font-family: "Arimo", Arial, sans-serif;
    overflow: hidden;
  }
  .heading {
    position: absolute;
    left: 69px; top: 60px;
    font-size: 30px;
  }
  .fill-line {
    position: absolute;
    left: 69px;
    width: 549px;
    height: 2px;
    background: var(--ink);
  }
  .fill-line--one { top: 152px; }
  .fill-line--two { top: 220px; }
  .on-label {
    position: absolute;
    left: 69px; top: 264px;
    font-size: 28px;
  }
  .day {
    position: absolute;
    display: flex;
    align-items: center;
    font-family: "Roboto Condensed", "Arial Narrow", sans-serif;
    font-size: 33px;
  }
  .day::before {
    content: "";
    width: 32px; height: 32px;
    border: 2px solid var(--ink);
    margin-right: 10px;
  }
  .row-1 { top: 307px; }
  .row-2 { top: 355px; }
  .col-1 { left: 69px; }
  .col-2 { left: 237px; }
  .col-3 { left: 385px; }
  .when {
    position: absolute;
    left: 69px; top: 425px;
    width: 549px;
    display: flex;
    align-items: flex-end;
    font-size: 30px;
  }
  .when .blank {
    height: 2px;
    background: var(--ink);
    margin-bottom: 6px;
  }
  .blank--date { width: 164px; margin: 0 2px 6px 8px; }
  .blank--time { flex: 1; margin-left: 10px; }
  .policy {
    position: absolute;
    left: 69px; top: 524px;
    width: 570px;
    font-family: "Roboto Condensed", "Arial Narrow", sans-serif;
    font-size: 32px;
    line-height: 41px;
  }
  .wave {
    position: absolute;
    left: 0; top: 0;
    width: 686px; height: 1200px;
  }
  .reminder {
    position: absolute;
    left: 67px; top: 868px;
    width: 600px;
    color: var(--paper);
  }
  .reminder__title {
    font-weight: 700;
    font-size: 28px;
    color: var(--highlight);
    line-height: 36px;
  }
  .reminder__body {
    font-family: "Roboto Condensed", "Arial Narrow", sans-serif;
    font-size: 31px;
    line-height: 41px;
  }
  .reminder__cta {
    margin-top: 18px;
    font-weight: 700;
    font-size: 31px;
    line-height: 45px;
  }
</style>
</head>
<body>
<main class="card">
  <svg class="wave" viewBox="0 0 686 1200" aria-hidden="true">
    <defs>
      <linearGradient id="bandBlue" x1="0" y1="0" x2="1" y2="0">
        <stop offset="0" stop-color="#0a3c9e"/>
        <stop offset="1" stop-color="#3a8ee3"/>
      </linearGradient>
      <linearGradient id="bandAqua" x1="0" y1="0" x2="1" y2="0">
        <stop offset="0" stop-color="#a8f3ec"/>
        <stop offset="1" stop-color="#d9fbf7"/>
      </linearGradient>
    </defs>
    <path d="M0,718 C160,800 290,820 430,768 C540,726 620,690 686,686 L686,1200 L0,1200 Z" fill="url(#bandAqua)"/>
    <path d="M0,740 C170,830 300,840 440,790 C550,750 630,715 686,712 L686,1200 L0,1200 Z" fill="url(#bandBlue)"/>
  </svg>

  <p class="heading">Next Appointment is for:</p>
  <div class="fill-line fill-line--one"></div>
  <div class="fill-line fill-line--two"></div>

  <p class="on-label">on:</p>
  <span class="day row-1 col-1">Mon</span>
  <span class="day row-1 col-2">Tue</span>
  <span class="day row-1 col-3">Wed</span>
  <span class="day row-2 col-1">Thu</span>
  <span class="day row-2 col-2">Fri</span>
  <span class="day row-2 col-3">Sat</span>

  <div class="when">
    <span>Date:</span><span class="blank blank--date"></span>
    <span>Time:</span><span class="blank blank--time"></span>
  </div>

  <p class="policy">A broken appointment is a loss for everyone. Please inform us 24 hours in advance if you are unable to keep your appointment or you may be charged for a missed visit.</p>

  <section class="reminder">
    <p class="reminder__title">Please remember:</p>
    <p class="reminder__body">Nothing to eat or drink 6 hours prior to IV Sedation. Bring any necessary x-rays, medications, and referral slips.</p>
    <p class="reminder__cta">Save time by filling out your<br>Medical history online.</p>
  </section>
</main>
</body>
</html>
```